Poster for pawn shop lobby

Looking for green and gold as my colors, like the picture shown of my old poster. This time I'm contemplating with doing pictures as well as just text. Here are ideas of things I buy and give loans on. We want to emphasize jewelry, laptops, game systems, tools. I'm open-minded.
Old & Broken Gold
Jewelry & Collectibles
Diamonds
Video Games & Systems
Up-to-date Computers & Laptops
Tablets
Cameras
Power Tools
Home & Garden Equipment
Sports Equipment
Watches
Antique Collectibles
Musical Instruments
And anything else of value
Shop

```html
<!DOCTYPE html>
<html lang="en">
<head>
<meta charset="utf-8">
<title>We'll Loan or Pay You Cash – Pawn Shop Poster</title>
<link rel="stylesheet" href="https://fonts.googleapis.com/css2?family=Ultra&family=Quattrocento:wght@700&display=swap">
<style>
  :root {
    --green-top: #2f6e3b;
    --green-mid: #0d7a4c;
    --green-bottom: #0c4634;
    --gold: #c9a33a;
    --white: #ffffff;
    --outline: #12382a;
    --yellow: #f7e81c;
    --photo-light: #e9e6e1;
    --photo-mid: #a39a90;
    --photo-dark: #4a3f38;
  }
  html, body {
    margin: 0;
    padding: 0;
    overflow: hidden;
  }
  .poster {
    position: relative;
    width: 849px;
    height: 1200px;
    overflow: hidden;
    background: linear-gradient(180deg, var(--green-top) 0%, var(--green-mid) 42%, var(--green-mid) 60%, var(--green-bottom) 100%);
  }
  .headline {
    position: absolute;
    left: 0;
    top: 0;
    width: 849px;
    height: 340px;
  }
  .headline text {
    paint-order: stroke;
    stroke: var(--outline);
    stroke-linejoin: round;
  }
  .headline .script {
    font-family: 'Ultra', serif;
    fill: var(--white);
    stroke-width: 3;
  }
  .headline .accent {
    font-family: 'Quattrocento', serif;
    font-weight: 700;
    fill: var(--gold);
    stroke-width: 3;
  }
  .merchandise {
    position: absolute;
    left: 100px;
    top: 335px;
    width: 656px;
    height: 502px;
    background:
      radial-gradient(ellipse at 75% 80%, #b08a3a 0%, rgba(176,138,58,0) 35%),
      radial-gradient(ellipse at 30% 85%, #6d6a68 0%, rgba(109,106,104,0) 40%),
      linear-gradient(180deg, var(--photo-light) 0%, var(--photo-mid) 45%, var(--photo-dark) 100%);
    -webkit-mask-image: radial-gradient(ellipse 62% 60% at 50% 50%, #000 70%, transparent 100%);
    mask-image: radial-gradient(ellipse 62% 60% at 50% 50%, #000 70%, transparent 100%);
  }
  .item-list {
    position: absolute;
    left: 0;
    top: 872px;
    width: 849px;
    margin: 0;
    text-align: center;
    font-family: 'Quattrocento', serif;
    font-weight: 700;
    font-size: 33px;
    line-height: 47px;
    color: var(--yellow);
    text-shadow: 1px 1px 1px rgba(0,0,0,0.35);
  }
  .item-list span {
    display: block;
    white-space: nowrap;
  }
</style>
</head>
<body>
<main class="poster">
  <svg class="headline" viewBox="0 0 849 340" aria-label="We'll loan or pay you cash">
    <defs>
      <path id="arc-loan" d="M -60 612 A 501 501 0 0 1 942 612"/>
      <path id="arc-pay" d="M 103 525 A 330 330 0 0 1 763 525"/>
      <path id="arc-cash" d="M -442 1214 A 900 900 0 0 1 1358 1214"/>
    </defs>
    <text text-anchor="middle">
      <textPath href="#arc-loan" startOffset="50%">
        <tspan class="script" font-size="66">We’ll </tspan><tspan class="accent" font-size="112">LOAN</tspan>
      </textPath>
    </text>
    <text class="script" font-size="64" text-anchor="middle">
      <textPath href="#arc-pay" startOffset="50%">or pay you</textPath>
    </text>
    <text class="accent" font-size="108" text-anchor="middle">
      <textPath href="#arc-cash" startOffset="50%">CASH</textPath>
    </text>
  </svg>

  <div class="merchandise" role="img" aria-label="Collage of pawn items: modern kitchen with cookware, exercise bikes, speakers, electric guitar, laptop and a treasure chest spilling gold jewelry"></div>

  <p class="item-list">
    <span>Old &amp; Broken Gold,</span>
    <span>Jewelry &amp; Antique Collectibles, Diamonds,</span>
    <span>Video Games &amp; Systems, Up-to-date Computers</span>
    <span>&amp; Laptops, Tablets, Cameras, Power Tools,</span>
    <span>Home &amp; Garden Equipment, Sports Equipment,</span>
    <span>Watches, Musical Instruments,</span>
    <span>And anything else of value</span>
  </p>
</main>
</body>
</html>
```